An anniversary gift for my girlfriend

My girlfriend and I have been dating for almost 2 years. We met online and this has afforded us the really unique opportunity to have the first words we said to each other (the whole conversation, in fact) preserved. We're moving in together in a few months and she doesn't know that I saved the conversation. I've been waiting for this to turn it into something we can hang in our new place.

The only phrase I want to use is:
"Well if you dislike people's knees then I think we'll get along famously"

It's an Nobody Leaves Before Midnight in Portland reference for the curious.

I want the poster to use the words themselves as the art; I'm thinking typography. I'd like it to match her aesthetic, she likes to wear Nora Vell and T. Brisk. Colors shouldn't be anything too "girly". Somewhere I'd like to include the date June 1, 2015. It shouldn't be a major piece of the poster though, just a way to denote the date.

It should fit (and be fully visible in) a 16x20 (inches) frame

Thanks in advance for the work!

Requirements
Must have
• Must use only the words: "Well if you dislike people's knees then I think we'll get along famously"
• I want this to be typography, so making the phrase the center of the poster and the art itself.

```html
<!DOCTYPE html>
<html lang="en">
<head>
<meta charset="utf-8">
<title>Well If You Dislike People's Knees</title>
<link rel="stylesheet" href="https://fonts.googleapis.com/css2?family=Prata&family=Federo&display=swap">
<style>
  :root {
    --paper: #fdf9ea;
    --frame: #a9d7d5;
    --panel: #acd8d6;
    --moss: #3b4a2f;
    --rust: #a6432a;
    --brick: #98401f;
    --ink-blue: #2f5d87;
    --poppy: #e03a3b;
    --charcoal: #333533;
    --plum: #a4508f;
    --slate: #5a6a94;
    --coral: #f08769;
    --outline: #4d6673;
  }
  html, body {
    margin: 0;
    padding: 0;
    width: 960px;
    height: 1200px;
    overflow: hidden;
    background: var(--paper);
  }
  .poster {
    position: relative;
    width: 960px;
    height: 1200px;
    background: var(--paper);
    font-family: "Prata", Georgia, serif;
  }
  .frame-outer {
    position: absolute;
    left: 40px; top: 40px;
    width: 880px; height: 1028px;
    border: 6px solid var(--frame);
    border-radius: 50px;
    box-sizing: border-box;
  }
  .frame-panel {
    position: absolute;
    left: 62px; top: 62px;
    width: 836px; height: 984px;
    background: var(--panel);
    border-radius: 30px;
    overflow: hidden;
  }
  .shapes {
    position: absolute;
    left: 0; top: 0;
    width: 960px; height: 1200px;
  }
  .art {
    position: absolute;
    border-radius: 14px;
  }
  .art-piano { left: 456px; top: 173px; width: 106px; height: 144px; background: linear-gradient(160deg, #d7ecea, #6fb9b4); opacity: .8; }
  .art-blossoms-top { left: 668px; top: 106px; width: 230px; height: 250px; background: linear-gradient(180deg, #f3a082, #e9977a); opacity: .85; border-radius: 40px 0 0 40px; }
  .art-blossoms-side { left: 792px; top: 356px; width: 106px; height: 200px; background: linear-gradient(180deg, #e9977a, #f2a98c); opacity: .85; border-radius: 40px 0 0 40px; }
  .art-flourish-left { left: 152px; top: 260px; width: 52px; height: 88px; background: #4f6146; opacity: .45; }
  .art-flourish-right { left: 768px; top: 798px; width: 58px; height: 60px; background: #4f5f8a; opacity: .4; }
  .art-balloon { left: 88px; top: 555px; width: 92px; height: 88px; background: var(--coral); border-radius: 46px; }
  .art-bicycle { left: 50px; top: 869px; width: 392px; height: 272px; background: linear-gradient(180deg, #e8e9d8, #b9bcae); opacity: .9; border-radius: 30px; }
  .art-dove { left: 754px; top: 907px; width: 92px; height: 110px; background: #8f95d2; opacity: .5; }

  .phrase {
    margin: 0;
    font-weight: 400;
  }
  .phrase .word {
    position: absolute;
    white-space: nowrap;
    line-height: 1;
  }
  .w-well { left: 212px; top: 234px; font-size: 100px; color: var(--moss); }
  .w-if { left: 401px; top: 318px; font-size: 76px; color: var(--moss); font-family: "Federo", "Prata", serif; letter-spacing: -4px; }
  .w-you { left: 446px; top: 344px; font-size: 56px; color: var(--moss); }
  .w-dislike { left: 240px; top: 392px; font-size: 52px; letter-spacing: 3px; color: var(--rust); }
  .w-peoples { left: 374px; top: 444px; font-size: 74px; letter-spacing: 3px; color: var(--rust); }
  .w-knees { left: 251px; top: 516px; font-size: 60px; letter-spacing: 1px; color: var(--ink-blue); }
  .w-then { left: 320px; top: 576px; font-size: 62px; color: var(--brick); font-family: "Federo", "Prata", serif; letter-spacing: -3px; }
  .w-i { left: 466px; top: 560px; font-size: 80px; color: var(--moss); font-family: "Federo", "Prata", serif; }
  .w-think { left: 499px; top: 527px; font-size: 101px; color: var(--poppy); }
  .w-well-get { left: 346px; top: 643px; font-size: 68px; color: var(--charcoal); }
  .w-along { left: 184px; top: 696px; font-size: 72px; color: var(--plum); }
  .w-famously { left: 394px; top: 723px; font-size: 78px; color: var(--slate); }
</style>
</head>
<body>
<main class="poster">
  <div class="frame-outer"></div>
  <div class="frame-panel"></div>

  <svg class="shapes" viewBox="0 0 960 1200" aria-hidden="true">
    <g fill="none" stroke="var(--outline)" stroke-width="1.2" opacity=".7">
      <circle cx="556" cy="109" r="12"/>
      <circle cx="805" cy="636" r="12"/>
      <circle cx="407" cy="899" r="12"/>
      <circle cx="213" cy="134" r="20"/>
      <circle cx="658" cy="348" r="20"/>
      <circle cx="838" cy="728" r="20"/>
      <circle cx="180" cy="899" r="20"/>
      <circle cx="644" cy="80" r="18"/>
    </g>
    <line x1="133" y1="640" x2="133" y2="990" stroke="#3a3a3a" stroke-width="1"/>
  </svg>

  <div class="art art-flourish-left" role="img" aria-label="Small leafy flourish ornament"></div>
  <div class="art art-piano" role="img" aria-label="Sketch of a grand piano"></div>
  <div class="art art-blossoms-top" role="img" aria-label="Coral flowers and a fern sprig in the top right corner"></div>
  <div class="art art-blossoms-side" role="img" aria-label="Coral flowers along the right edge"></div>
  <div class="art art-balloon" role="img" aria-label="Heart-shaped balloon"></div>
  <div class="art art-flourish-right" role="img" aria-label="Small leafy flourish ornament"></div>
  <div class="art art-bicycle" role="img" aria-label="Illustrated vintage bicycle with a pink seat"></div>
  <div class="art art-dove" role="img" aria-label="Dotted outline of a small bird"></div>

  <h1 class="phrase" aria-label="Well if you dislike people's knees then I think we'll get along famously">
    <span class="word w-well">Well</span>
    <span class="word w-if">If</span>
    <span class="word w-you">You</span>
    <span class="word w-dislike">Dislike</span>
    <span class="word w-peoples">People's</span>
    <span class="word w-knees">Knees</span>
    <span class="word w-then">Then</span>
    <span class="word w-i">I</span>
    <span class="word w-think">Think</span>
    <span class="word w-well-get">We'll Get</span>
    <span class="word w-along">Along</span>
    <span class="word w-famously">Famously</span>
  </h1>
</main>
</body>
</html>
```